FOLI PACK FOR STICKS

Design the packaging for salted sticks (weight 400g) reference to the logo TOVEN (in attached).
Color packaging- look forward to suggestions.
Package with window.
Hi, we need only graphic conception without texts on back side.

Please find Logo TOVEN and the grid of packaging - attached
Updates

we need only graphic conception without texts on back side. Added Saturday, November 08, 2014

Target Market(s)

typical salted snack for everyone (adults and children included)

Font styles to use
Sans Serif

Requirements
Should not have
• - religion and politic signs…
• - toys and childdraws
• - monsters, devils and demons etc.

```html
<!DOCTYPE html>
<html lang="en">
<head>
<meta charset="utf-8">
<title>Salty Pretzel Sticks – Foil Pack</title>
<link rel="stylesheet" href="https://fonts.googleapis.com/css2?family=Montserrat:wght@400;600;700&family=Playfair+Display:wght@900&display=swap">
<style>
  :root {
    --backdrop: #a99b80;
    --pack-top: #1b1816;
    --pack-mid: #3b2e24;
    --pack-bottom: #8c7155;
    --pack-base: #a2896b;
    --title-red: #b3161b;
    --title-white: #e9e6e2;
    --brand-gold: #c9a24a;
    --pretzel-dark: #3a2214;
    --pretzel-mid: #7a4a27;
    --pretzel-light: #b37a45;
  }
  html, body {
    margin: 0;
    padding: 0;
    width: 1200px;
    height: 1200px;
    overflow: hidden;
    background: var(--backdrop);
  }
  .canvas {
    position: relative;
    width: 1200px;
    height: 1200px;
  }
  .pack {
    position: absolute;
    left: 340px;
    top: 220px;
    width: 533px;
    height: 767px;
    background: linear-gradient(to bottom,
      var(--pack-top) 0%,
      var(--pack-mid) 32%,
      #5a4431 55%,
      var(--pack-bottom) 78%,
      var(--pack-base) 100%);
    overflow: hidden;
  }
  .pack-seal {
    position: absolute;
    left: 0;
    right: 0;
    height: 20px;
    background: rgba(0, 0, 0, 0.25);
  }
  .pack-seal--top { top: 0; }
  .pack-seal--bottom { bottom: 0; background: rgba(90, 66, 44, 0.35); }
  .title-salty {
    position: absolute;
    left: 30px;
    top: 92px;
    margin: 0;
    font-family: "Montserrat", sans-serif;
    font-weight: 700;
    font-size: 44px;
    line-height: 1;
    color: var(--title-white);
    letter-spacing: 1px;
    transform: rotate(-14deg);
    transform-origin: left bottom;
  }
  .title-pretzel {
    position: absolute;
    left: 0;
    right: 0;
    top: 112px;
    margin: 0;
    padding-left: 70px;
    font-family: "Playfair Display", serif;
    font-weight: 900;
    font-size: 78px;
    line-height: 1;
    color: var(--title-red);
    letter-spacing: 1px;
    text-align: center;
  }
  .title-sticks {
    position: absolute;
    left: 0;
    right: 0;
    top: 180px;
    margin: 0;
    padding-right: 40px;
    font-family: "Montserrat", sans-serif;
    font-weight: 600;
    font-size: 34px;
    line-height: 1;
    color: var(--title-white);
    letter-spacing: 9px;
    text-align: center;
  }
  .pretzel-window {
    position: absolute;
    left: 10px;
    top: 228px;
    width: 513px;
    height: 325px;
  }
  .brand-name {
    position: absolute;
    left: 0;
    right: 0;
    top: 604px;
    margin: 0;
    font-family: "Montserrat", sans-serif;
    font-weight: 700;
    font-size: 50px;
    line-height: 1;
    color: var(--brand-gold);
    letter-spacing: 2px;
    text-align: center;
  }
  .net-weight {
    position: absolute;
    left: 0;
    right: 0;
    top: 676px;
    margin: 0;
    font-family: "Montserrat", sans-serif;
    font-weight: 400;
    font-size: 14px;
    line-height: 1;
    color: var(--title-white);
    text-align: center;
  }
</style>
</head>
<body>
<main class="canvas">
  <section class="pack">
    <div class="pack-seal pack-seal--top"></div>
    <p class="title-salty">SALTY</p>
    <h1 class="title-pretzel">PRETZEL</h1>
    <p class="title-sticks">sticks</p>

    <svg class="pretzel-window" viewBox="0 0 513 325" role="img"
         aria-label="Illustration of a large baked pretzel framing a window that shows pretzel sticks inside, with a golden horizontal band">
      <defs>
        <radialGradient id="pretzel-tone" cx="50%" cy="45%" r="60%">
          <stop offset="0%" stop-color="#7a4a27"/>
          <stop offset="60%" stop-color="#3a2214"/>
          <stop offset="100%" stop-color="#b37a45" stop-opacity="0.4"/>
        </radialGradient>
      </defs>
      <rect x="0" y="0" width="513" height="325" rx="140" fill="url(#pretzel-tone)"/>
    </svg>

    <p class="brand-name">TOVEN</p>
    <p class="net-weight">weight 400g</p>
    <div class="pack-seal pack-seal--bottom"></div>
  </section>
</main>
</body>
</html>
```